Can you make FairlyKind look better than average? We need business cards and a logo refresh :-)

REVISED BRIEF

PRIORITY

VECTOR LOGO

Create a vector version of our existing logo. The logo must not change from its current design, weight or font.

Deliverables

- Logo in blue (#2540BB)
- Logo in white (#FFFFFF)
- Logo in grey (#36454F)
- All logos on transparent background
- All logos in PNG & SVG formats. (SVG must NOT distort stroke width when resized)

BRAND MARK

Create a brand mark for use with the logo. This should be possible to used with the logo and on its own as a stand alone graphical device that represents the FairlyKind brand.

https://sitecrafter.example.com/resources/glossary/what-is-a-brand-mark

Deliverables

- Brand Mark in blue (#2540BB)
- Brand Mark in white (#FFFFFF)
- Brand Mark in grey (#36454F)
- Brand Mark on transparent background
- Brand Mark in PNG & SVG formats. (SVG must NOT distort stroke width when resized)
- Logo combined with Brand Mark (colours and formats)
.

Business Card Layout

Create 2 layouts with the following details:-

Marcus Trent
Co-Founder & Chief Product Officer

marcus@fairlykind.example.nz
www.fairlykind.example.nz
0279816354

Callum Bryce
Founder & CEO

hello@fairlykind.example.nz
www.fairlykind.example.nz
021 948 6207

DESIGN CONSIDERATIONS

Create versions with ‘Shaping Names With Heart’ tag line incorporated within the design and without (maintain separation of logo from tag line)

- Create a version with and without the brand mark
- Keep it clean and simple but elevate the design with subtle design effects
- Consider use of raised spot gloss colour (this can be white on white for subtle or blue on blue or blue on white)
- Consider use of spot gloss colour (this can be white on white for subtle or blue on blue or blue on white)
- Consider use of letterpress indentation
- Ensure contact details are legible, use sans-serif font

PREVIOUS BRIEF

We need a business card design for our business FairlyKind. We are a purpose driven brand and media agency that helps brands and charities plan and buy traditional media campaigns (TV, Radio, Print, Outdoor etc). We give a significant amount of the media booking fees we receive from media vendors to charity in the name of our clients. https://www.socialnet.example.com/posts/wearefairlykind_giveback-fairlykind-shapingnameswithheart-activity-5820394716253849102-Xqzt

Our strapline is 'Shaping Names With Heart'.

We want to keep our logo design as it is but it does need tightening up and made into a proper vector image as it's been created from a font.

Our brand colour is #2540BB and we need to keep this.

Our brand is professional but human, warm and engaging and doesn't take itself too seriously.

Things We Need
- vectorisation and tidying up of existing logo
- We'd like you to think about how we can incorporate a brand mark with the logo to add another dimension to our brand
- business card layout and design
- we'll be using cardloop.example.com to print the cards so please take a look at the options they have (spot gloss, foil, letterpress, square cards and even the backs of the cards can have a different design on every single card!
- potential opportunity for different famous quotes on the back or imagery or slight design differences
- we'd be open to the use of an emoji or emojiis as the brandmark or to be incorporated into the card designs
- we can have as many different design batches as we like for the backs of the cards

https://www.cardloop.example.com/au/business-cards

We want to make an impact, we want to be seen as professional but fun, we want to be different.

Here's a press release of what we're about.

https://adwirenews.example.co.nz/movings-shakings/fairlykind-welcomes-marcus-trent-as-co-founder/

Be bold, be different, there is no such thing as a bad idea. We're open to anything so please bring your best ideas and have fun with it! Go crazy if you like!
____________
Marcus Trent
marcus@fairlykind.example.nz
0279816354

Callum Bryce
Founder & CEO
hello@fairlykind.example.nz
021 948 6207

Shaping Names With Heart

________

These are the only details we MUST have on the cards, the rest is up to you. Just make sure you use all of your creativity but don't feel the need to crowd the card with too much, let it breathe as well.

In terms of font for the details, we'll leave that up to you, just ensure it's legible. Oh and please don't take any design inspiration from our website - that will be changing!

Please don't let the design and layout look cheap and tacky though. It needs to still feel premium but personable.

Thanks

Marcus
Updates

Many designs are changing the logo and this was NOT in the brief. We need a brand mark to complement the logo. We need to see the logo with and without the brand mark. We need to see the business card with both logo + brand mark and logo on its own We need to see the business card with and without the tagline 'Shaping Names With Heart'

Industry/Entity Type

purpose driven Brand & Media Agency

Contact Information for Business Card

Shaping Names With Heart
Marcus Trent, Co-Founder & Chief Product Officer, marcus@fairlykind.example.nz fairlykimd.example.nz, 0279 816 354

Callum Bryce, Founder & CEO hello@fairlykind.example.nz, fairlykimd.example.nz, 021 948 6207

Font styles to use
Serif
Sans Serif

Colors
0054AA
0677BA
7BADD7
CADEEF
E8F1F8

Requirements
Must have
• brand mark, vector version of existing logo, Shaping Names With Heart tagline, existing logo traced and vectorised. Must fully explore the design options from cardloop.example.com that can enhance the overall card design
Nice to have
• brandmark to help elevate the logo, maybe incorporate some other design elements into the card like lines, or grids.
Should not have
• A cheap look and feel

```html
<!DOCTYPE html>
<html lang="en">
<head>
<meta charset="utf-8">
<title>FairlyKind Business Card</title>
<link rel="stylesheet" href="https://fonts.googleapis.com/css2?family=Montserrat:wght@400;500;600;700&display=swap">
<style>
  :root{
    --brand-blue:#3a4fa8;
    --brand-blue-deep:#2f44a0;
    --brand-blue-light:#5566b8;
    --ink:#222222;
    --card-white:#ffffff;
    --stage:#e9e9ec;
  }
  *{margin:0;padding:0;box-sizing:border-box}
  html,body{width:1200px;height:786px;overflow:hidden}
  body{background:var(--stage);font-family:"Montserrat",Arial,sans-serif;position:relative}
  .card{position:absolute;top:244px;width:520px;height:298px;overflow:hidden;box-shadow:0 10px 28px rgba(0,0,0,.18)}
  .card--back{left:60px;background:var(--brand-blue)}
  .card--front{left:620px;background:var(--card-white)}

  .back-texture{position:absolute;inset:0;background:linear-gradient(135deg,var(--brand-blue-deep) 0%,var(--brand-blue) 55%,var(--brand-blue-light) 100%)}
  .back-wordmark{position:absolute;left:0;right:0;top:126px;text-align:center;font-weight:600;font-size:40px;color:rgba(255,255,255,.16)}

  .front-wave{position:absolute;inset:0}
  .wordmark{position:absolute;left:64px;top:44px;font-weight:600;font-size:44px;line-height:1;color:var(--brand-blue)}

  .person{position:absolute;left:36px;top:120px;width:210px;text-align:right}
  .person__name{font-weight:700;font-size:19px;color:var(--brand-blue)}
  .person__role{font-size:10.5px;color:var(--ink);margin-top:3px}
  .divider{position:absolute;left:258px;top:112px;width:1.5px;height:54px;background:var(--brand-blue)}
  .contacts{position:absolute;left:270px;top:108px;list-style:none;font-size:10.5px;color:var(--ink)}
  .contacts li{display:flex;align-items:center;gap:8px;height:19px}
  .contacts svg{width:11px;height:11px;fill:var(--brand-blue);flex:none}

  .tagline{position:absolute;left:40px;bottom:22px;font-size:11.5px;font-weight:500;color:var(--card-white)}
</style>
</head>
<body>
  <section class="card card--back" aria-label="Card back">
    <div class="back-texture" role="img" aria-label="Blue field with a grid of small glossy squares"></div>
    <div class="back-wordmark">FairlyKind</div>
  </section>

  <section class="card card--front" aria-label="Card front">
    <svg class="front-wave" viewBox="0 0 520 298" aria-hidden="true">
      <path d="M0,298 L0,236 C110,184 250,216 380,200 C450,190 500,160 520,128 L520,298 Z" fill="var(--brand-blue)"/>
      <path d="M320,204 C420,194 490,166 520,116" fill="none" stroke="var(--brand-blue)" stroke-width="2.5"/>
    </svg>

    <div class="wordmark">FairlyKind</div>

    <div class="person">
      <div class="person__name">Marcus Trent</div>
      <div class="person__role">Co-Founder &amp; Chief Product Officer</div>
    </div>
    <div class="divider"></div>
    <ul class="contacts">
      <li><svg viewBox="0 0 24 24"><path d="M6.6 10.8a15 15 0 0 0 6.6 6.6l2.2-2.2a1 1 0 0 1 1-.25 11.4 11.4 0 0 0 3.6.57 1 1 0 0 1 1 1V20a1 1 0 0 1-1 1A17 17 0 0 1 3 4a1 1 0 0 1 1-1h3.5a1 1 0 0 1 1 1c0 1.25.2 2.45.57 3.57a1 1 0 0 1-.25 1z"/></svg>0279 816 354</li>
      <li><svg viewBox="0 0 24 24"><path d="M2 5h20v14H2z M4 7l8 6 8-6" fill="none" stroke="var(--brand-blue)" stroke-width="2.4"/></svg>marcus@fairlykind.example.nz</li>
      <li><svg viewBox="0 0 24 24"><circle cx="12" cy="12" r="9" fill="none" stroke="var(--brand-blue)" stroke-width="2.2"/><path d="M3 12h18M12 3c3 3 3 15 0 18M12 3c-3 3-3 15 0 18" fill="none" stroke="var(--brand-blue)" stroke-width="1.8"/></svg>www.fairlykind.example.nz</li>
    </ul>

    <div class="tagline">Shaping Names With Heart</div>
  </section>
</body>
</html>
```